Plakatwand für Werbeagentur
Zielgruppe
Wir sind eine Werbeagentur und möchten auf der Plakatwerbung vor allem Webdesign bewerben.
Die Plakatwand wird vor Weihnachten bzw. zwischen den Jahren gespielt. Denkbar wäre auch das Motto – neues Jahr neue Webseite, muss aber nicht sein.
Bitte die Webseite, das Social-Media PRofil aufführen sowie den Ort Dammbach (Anbieter aus der Region)
Aufgabenstellung
Plakatwand 590 mm x 410 mm (Maßstab 1:6), kein Beschnitt,
keine Beschnittzeichen, Sicherheitsabstand 2 cm zum Rand
Bitte Bildmaterial von Velkor Bilder vorschlagen, wird von uns gekauft
Schriftart Futura PT

```html
<!DOCTYPE html>
<html lang="de">
<head>
<meta charset="utf-8">
<title>norva.kreativ – Plakat Webdesign</title>
<link href="https://fonts.googleapis.com/css2?family=Jost:wght@300;500;600&display=swap" rel="stylesheet">
<style>
  :root {
    --bg: #e9e9e9;
    --paper: #f7f7f7;
    --ink: #111111;
    --grey-word: #555555;
    --green: #93c68e;
    --green-soft: #c4e3bd;
    --green-pale: #eef7ec;
    --green-line: #e3f1e0;
    --photo-dark: #3a3833;
    --photo-warm: #b7a77f;
  }
  html, body {
    margin: 0;
    width: 1200px;
    height: 1200px;
    overflow: hidden;
    background: var(--bg);
    font-family: "Jost", "Futura", sans-serif;
  }
  .poster {
    position: absolute;
    left: 125px;
    top: 247px;
    width: 965px;
    height: 694px;
    background: linear-gradient(135deg, #ffffff 0%, var(--paper) 60%, #f1f1f1 100%);
    overflow: hidden;
  }
  .devices-visual {
    position: absolute;
    left: 73px;
    top: 38px;
    width: 776px;
    height: 376px;
    background: linear-gradient(160deg, var(--photo-dark) 0%, var(--photo-warm) 45%, #8d897f 70%, #dcdcdc 100%);
    clip-path: polygon(0 190px, 180px 190px, 180px 0, 592px 0, 592px 170px, 776px 170px, 776px 376px, 0 376px);
  }
  .brand {
    position: absolute;
    left: 720px;
    top: 66px;
    width: 174px;
    text-align: center;
  }
  .brand-dot {
    display: block;
    width: 60px;
    height: 60px;
    margin: 0 auto 14px;
    border-radius: 50%;
    background: var(--green);
  }
  .brand-name {
    font-weight: 300;
    font-size: 31px;
    line-height: 1;
    color: var(--ink);
    white-space: nowrap;
  }
  .headline span {
    position: absolute;
    line-height: 1;
    white-space: nowrap;
  }
  .line-small {
    font-weight: 600;
    font-size: 46px;
    color: var(--ink);
  }
  .line-big {
    font-weight: 500;
    letter-spacing: -1px;
  }
  .we-create { left: 80px; top: 437px; }
  .website { left: 117px; top: 477px; font-size: 89px; color: var(--grey-word); }
  .that-build { left: 471px; top: 450px; }
  .your { left: 471px; top: 512px; }
  .business { left: 572px; top: 479px; font-size: 86px; color: var(--green); }
  .divider {
    position: absolute;
    left: 418px;
    top: 449px;
  }
  .contact-band {
    position: absolute;
    left: 0;
    top: 580px;
    width: 965px;
    height: 92px;
    background: linear-gradient(90deg, var(--green-pale) 0%, #dcefd7 50%, var(--green-soft) 100%);
  }
  .base-stripe {
    position: absolute;
    left: 0;
    top: 672px;
    width: 965px;
    height: 22px;
    background: var(--green);
  }
  .contact {
    position: absolute;
    display: flex;
    align-items: center;
    gap: 14px;
    font-weight: 500;
    font-size: 20px;
    color: var(--ink);
    white-space: nowrap;
    line-height: 20px;
  }
  .contact svg { width: 20px; height: 20px; flex: none; }
  .col-1 { left: 54px; }
  .col-2 { left: 365px; }
  .col-3 { left: 576px; }
  .row-1 { top: 600px; }
  .row-2 { top: 636px; }
</style>
</head>
<body>
  <div class="poster">
    <div class="devices-visual" role="img" aria-label="Foto: Responsive Webseite auf Desktop-Monitor, Laptop, Tablet und Smartphone"></div>

    <div class="brand">
      <span class="brand-dot"></span>
      <div class="brand-name">norva.kreativ</div>
    </div>

    <div class="headline">
      <span class="line-small we-create">We Create</span>
      <span class="line-big website">Website</span>
      <span class="line-small that-build">That Build</span>
      <span class="line-small your">Your</span>
      <span class="line-big business">Business</span>
    </div>

    <svg class="divider" width="50" height="114" viewBox="0 0 50 114">
      <line x1="4" y1="4" x2="44" y2="109" stroke="var(--green-line)" stroke-width="6"/>
    </svg>

    <div class="contact-band"></div>
    <div class="base-stripe"></div>

    <div class="contact col-1 row-1">
      <svg viewBox="0 0 24 24"><circle cx="12" cy="12" r="12" fill="var(--green)"/><g fill="none" stroke="#fff" stroke-width="1.2"><circle cx="12" cy="12" r="7"/><ellipse cx="12" cy="12" rx="3" ry="7"/><line x1="5" y1="12" x2="19" y2="12"/><line x1="6" y1="8.5" x2="18" y2="8.5"/><line x1="6" y1="15.5" x2="18" y2="15.5"/></g></svg>
      <span>www.norvakreativ.de</span>
    </div>
    <div class="contact col-1 row-2">
      <svg viewBox="0 0 24 24"><circle cx="12" cy="12" r="12" fill="var(--green)"/><g fill="none" stroke="#fff" stroke-width="1.3"><rect x="6" y="8" width="12" height="8.5" rx="1"/><polyline points="6,8.5 12,13 18,8.5"/></g></svg>
      <span>kontakt@norva-kreativ.de</span>
    </div>
    <div class="contact col-2 row-1">
      <svg viewBox="0 0 24 24"><circle cx="12" cy="12" r="12" fill="var(--green)"/></svg>
      <span>Norva.kreativ</span>
    </div>
    <div class="contact col-2 row-2">
      <svg viewBox="0 0 24 24"><circle cx="12" cy="12" r="12" fill="var(--green)"/></svg>
      <span>norva.kreativ</span>
    </div>
    <div class="contact col-3 row-1">
      <svg viewBox="0 0 24 24"><circle cx="12" cy="12" r="12" fill="var(--green)"/><path d="M8.2 6.5l2 2.4-1.2 1.5c.8 1.7 2 2.9 3.7 3.7l1.5-1.2 2.4 2-1.3 2c-4.6-.4-8.5-4.3-8.9-8.9z" fill="#fff"/></svg>
      <span>06021 5550184</span>
    </div>
    <div class="contact col-3 row-2">
      <svg viewBox="0 0 24 24"><circle cx="12" cy="12" r="12" fill="var(--green)"/><path d="M12 5.5a4.5 4.5 0 0 1 4.5 4.5c0 3.3-4.5 8.5-4.5 8.5S7.5 13.3 7.5 10A4.5 4.5 0 0 1 12 5.5z" fill="none" stroke="#fff" stroke-width="1.4"/><circle cx="12" cy="10" r="1.6" fill="#fff"/></svg>
      <span>Lindenpfad 14 63899 Waldmark</span>
    </div>
  </div>
</body>
</html>
```